Verpackungsdesign für Dattelkernpulver gesucht
Zielgruppe
Zu uns: Wir sind Nuvo-Lind. Mit unserem Dattelkernpulver bieten wir jedem die Chance die Power der Dattelkerne aktiver in die Ernährung zu integrieren. Neugierigen sowie auch Dattelkennern helfen wir eine ausgewogene Ernährung zu erreichen – dank der sagenumwobenen gesundheitlichen Vorteile der Ajwa-Dattel aus dem Orient. 100% naturbelassen, nicht wärmebehandelt und aus unserer Überzeugung für eine gesunde Ernährung.
Zur Zielgruppe: 50% w/50% m, 30+, aus Deutschland, progressiv und leicht esoterisch, mittleres-höheres Einkommenslevel (EUR 45k+), tendenziell höherer Bildungsgrad, typischerweise 'Verdalis'-Sympathisanten
Aufgabenstellung
Allgemein: Das Produktetikett wird um ein kleines 150g-200g Glas herum angebracht und auf den Deckel ebenfalls ein Rundes Etikett angebracht – verbunden durch ein “Siegel” mit dem zuvorgenannten Hauptetikett.
Vorderseite: Eindeutig erkennbares Logo und Markenname. Auf ersten Blick zu erkennen, dass es sich um Dattelkernpulver handelt ('Dattelkernpulver') inkl. einer Illustration die das leicht erkennen lässt. Deutliche Symbolik: 'Vegan', 'Laktosefrei', “ohne Konservierungsstoffe”, 'Ungezuckert', “Hergestellt in Deutschland”
Seite: Kleiner Blocktext mit 3-4 Zeilen mit kurzer Story zu unserer Überzeugung ('Die Power-Frucht aus 1001 Nacht: Dattelkernpulver von sorgfältig ausgewählten Premium Ajwa-Datteln aus Medina. 100% naturbelassen, nicht wärmebehandelt und aus unserer Überzeugung für ein gesundes Leben.') Zusätzlich eine Verzehrempfehlung ('Als täglicher Begleiter Deiner gesunden Ernährung je morgens einen Teelöffel.')
Rückseite: sehr leicht aufzufindende Zutatenliste sowie ein Dummy für die Nährwerttabelle. Kleiner Hinweis weiter unten auf Rückseite zur Marke (ähnlich wie private label 'kp Hausqualität') mit Kontaktdaten (Webseite, Email, Standort), dass unsere Transparenz und Erreichbarkeit vermittelt.
Oberseite: Label geht mit 'Siegel' bis auf den runden Deckel. Auf Oberseite Logo und schnell identifizierbarer Produktname.
Bitte beachten: Keine Kreuze, keine Dreiecke, nicht zu verspielt.
** Vielen Dank - ich freue mich auf Deinen spannenden Vorschlag! **
Maße:
-> Label: Breite 230mm, Höhe 30mm
-> Deckel: 50mm Druchmesser
-> Lasche vom Deckel zum Label: Breite ca. 10mm-15mm

```html
<!DOCTYPE html>
<html lang="de">
<head>
<meta charset="utf-8">
<title>Nuvo-Lind Dattelkernpulver – Etikett</title>
<link rel="stylesheet" href="https://fonts.googleapis.com/css2?family=Encode+Sans+Condensed:wght@400;500&family=Open+Sans:wght@400;700&display=swap">
<style>
  :root {
    --blue: #1b87c9;
    --blue-faint: #dbe7f4;
    --green: #5f9a1f;
    --green-dark: #4d8a17;
    --white: #ffffff;
    --bg: #ffffff;
    --date-dark: #4a3b33;
    --date-light: #c08a4a;
  }
  * { margin: 0; padding: 0; box-sizing: border-box; }
  html, body { width: 1200px; height: 730px; overflow: hidden; background: var(--bg); }
  body { position: relative; font-family: "Encode Sans Condensed", sans-serif; color: var(--blue); }

  /* Main wrap-around label */
  .main-label {
    position: absolute; left: 29px; top: 71px; width: 1142px; height: 148px;
    background: var(--white);
    border-top: 6px solid var(--blue);
    border-bottom: 5px solid var(--green);
    box-shadow: 0 3px 5px rgba(0,0,0,0.25);
    overflow: hidden;
  }
  .label-crescent { position: absolute; left: 460px; top: -6px; width: 260px; height: 148px; }

  .nutrition { position: absolute; left: 12px; top: 14px; width: 148px; font-size: 10.5px; line-height: 15.4px; }
  .nutrition-head { display: flex; justify-content: space-between; border-bottom: 1px solid var(--blue); padding-bottom: 1px; margin-bottom: 6px; }
  .nutrition-row { display: flex; white-space: nowrap; overflow: hidden; }
  .nutrition-row .dots { flex: 1; overflow: hidden; }
  .nutrition-row .dots::before { content: "................................................................"; letter-spacing: 0.5px; }

  .ingredients { position: absolute; left: 232px; top: 14px; font-size: 10.5px; color: var(--green); }
  .contact { position: absolute; left: 205px; top: 62px; width: 120px; text-align: center; font-size: 10.5px; line-height: 13.5px; color: var(--green); }

  .badge { position: absolute; width: 24px; text-align: center; }
  .badge svg { display: block; width: 24px; height: 24px; }
  .badge span { display: block; font-size: 4px; line-height: 5px; color: var(--green); white-space: nowrap; margin-left: -6px; width: 36px; }

  .brand { position: absolute; display: flex; align-items: center; gap: 4px; color: var(--green); font-family: "Encode Sans Condensed", sans-serif; font-weight: 500; }
  .brand-dot { border-radius: 50%; background: var(--blue); }
  .product-title { position: absolute; font-family: "Open Sans", sans-serif; font-weight: 700; color: var(--green); letter-spacing: -0.2px; white-space: nowrap; }
  .product-sub { position: absolute; font-family: "Open Sans", sans-serif; color: var(--green); white-space: nowrap; }
  .dates-image { position: absolute; border-radius: 45% 50% 40% 50%; background: radial-gradient(ellipse at 35% 50%, var(--date-dark) 0 35%, var(--date-light) 60%, rgba(192,138,74,0) 72%); }

  .story { position: absolute; left: 782px; top: 16px; width: 352px; font-size: 10.2px; line-height: 13px; }
  .advice { position: absolute; left: 782px; top: 66px; font-size: 10.2px; color: var(--green); }
  .batch { position: absolute; left: 782px; top: 104px; font-size: 10.5px; line-height: 13.5px; }
  .storage { position: absolute; left: 977px; top: 104px; font-size: 10.5px; line-height: 13.5px; color: var(--green); }
  .weight { position: absolute; left: 1090px; top: 110px; font-family: "Open Sans", sans-serif; font-weight: 700; font-size: 20px; color: var(--green-dark); }

  /* Lid label with seal tab */
  .lid-label { position: absolute; left: 250px; top: 318px; width: 300px; height: 412px; }
  .lid-shape { position: absolute; left: 0; top: 0; width: 300px; height: 412px; }
</style>
</head>
<body>

<section class="main-label" aria-label="Hauptetikett">
  <svg class="label-crescent" viewBox="0 0 260 148" aria-hidden="true">
    <path d="M70 0 A120 120 0 0 0 225 148 L250 148 A125 125 0 0 1 100 0 Z" fill="var(--blue-faint)"/>
  </svg>

  <div class="nutrition">
    <div class="nutrition-head"><span>Nährwerte</span><span>in 100g</span></div>
    <div class="nutrition-row"><span>Brennwert&nbsp;</span><span class="dots"></span><span>330kcal/1234KJ</span></div>
    <div class="nutrition-row"><span>Kohlenhydrate&nbsp;</span><span class="dots"></span><span>80g</span></div>
    <div class="nutrition-row"><span>&nbsp;- davon Zucker&nbsp;</span><span class="dots"></span><span>5g</span></div>
    <div class="nutrition-row"><span>Fett&nbsp;</span><span class="dots"></span><span>3g</span></div>
    <div class="nutrition-row"><span>&nbsp;- davon gesättigte Fettsäuren&nbsp;</span><span class="dots"></span><span>0g</span></div>
    <div class="nutrition-row"><span>Eiweiß&nbsp;</span><span class="dots"></span><span>2g</span></div>
  </div>

  <div class="ingredients">Zutaten: Datteln</div>
  <address class="contact" style="font-style:normal">
    Nuvo-Lind<br>Mustermannstraße 1<br>12345 Musterstadt<br>www.nuvo-lind.de<br>info@nuvo-lind.de
  </address>

  <div class="badge" style="left:396px; top:16px;">
    <svg viewBox="0 0 24 24"><circle cx="12" cy="12" r="10.5" fill="none" stroke="var(--green)" stroke-width="1"/><path d="M7 13 C9 8 15 8 17 10 C14 11 11 13 7 13 Z" fill="none" stroke="var(--green)" stroke-width="1"/></svg>
    <span>vegan</span>
  </div>
  <div class="badge" style="left:429px; top:16px;">
    <svg viewBox="0 0 24 24"><circle cx="12" cy="12" r="10.5" fill="none" stroke="var(--green)" stroke-width="1"/><rect x="9" y="6" width="6" height="12" rx="1.5" fill="none" stroke="var(--green)" stroke-width="1"/><line x1="6" y1="18" x2="18" y2="6" stroke="var(--green)" stroke-width="1"/></svg>
    <span>laktosefrei</span>
  </div>

  <div class="brand" style="left:556px; top:18px; font-size:10px;"><span class="brand-dot" style="width:9px;height:9px;"></span>Nuvo-Lind</div>
  <div class="product-title" style="left:484px; top:42px; font-size:19px;">DATTELKERNPULVER</div>
  <div class="product-sub" style="left:534px; top:66px; font-size:8px;">aus Premium Ajwa Datteln</div>
  <div class="dates-image" role="img" aria-label="Foto zweier Ajwa-Datteln, eine aufgeschnitten mit Kern" style="left:550px; top:80px; width:62px; height:46px;"></div>

  <div class="badge" style="left:723px; top:16px;">
    <svg viewBox="0 0 24 24"><circle cx="12" cy="12" r="10.5" fill="none" stroke="var(--green)" stroke-width="1"/><rect x="8" y="7" width="8" height="11" rx="1" fill="none" stroke="var(--green)" stroke-width="1"/><line x1="6" y1="18" x2="18" y2="6" stroke="var(--green)" stroke-width="1"/></svg>
    <span>ohne Konservierung</span>
  </div>
  <div class="badge" style="left:756px; top:16px;">
    <svg viewBox="0 0 24 24"><circle cx="12" cy="12" r="10.5" fill="none" stroke="var(--green)" stroke-width="1"/><rect x="8" y="8" width="8" height="8" fill="none" stroke="var(--green)" stroke-width="1"/><line x1="6" y1="18" x2="18" y2="6" stroke="var(--green)" stroke-width="1"/></svg>
    <span>ungezuckert</span>
  </div>

  <p class="story">Die Power-Frucht aus 1001 Nacht: Dattelkernpulver von sorgfältig ausgewählten Premium Ajwa-Datteln aus Medina. 100% naturbelassen, nicht wärmebehandelt und aus unserer Überzeugung für ein gesundes Leben.</p>
  <p class="advice">Als täglicher Begleiter Deiner gesunden Ernährung je morgens einen Teelöffel.</p>
  <p class="batch">Charge: 18BAH1016<br>MHD: 02/2020</p>
  <p class="storage">Bitte trocken lagern.<br>Hergestellt in Deutschland</p>
  <p class="weight">150g</p>
</section>

<section class="lid-label" aria-label="Deckeletikett mit Siegellasche">
  <svg class="lid-shape" viewBox="0 0 300 412" aria-hidden="true">
    <rect x="135" y="200" width="58" height="212" fill="var(--blue)"/>
    <circle cx="147" cy="147" r="142" fill="var(--blue)"/>
    <circle cx="162" cy="132" r="122" fill="var(--white)"/>
  </svg>
  <div class="brand" style="left:148px; top:88px; font-size:9px;"><span class="brand-dot" style="width:8px;height:8px;"></span>Nuvo-Lind</div>
  <div class="product-title" style="left:96px; top:144px; font-size:16px;">DATTELKERNPULVER</div>
  <div class="product-sub" style="left:128px; top:165px; font-size:7.5px;">aus Premium Ajwa Datteln</div>
  <div class="dates-image" role="img" aria-label="Foto zweier Ajwa-Datteln, eine aufgeschnitten mit Kern" style="left:142px; top:184px; width:56px; height:44px;"></div>
</section>

</body>
</html>
```